Meridian Value Bourse (Account) WP Design

We need an Account (Profile) Wordpress design to add to mvb.co.uk.

The design should be based on https://mvb.co.uk/about/. The look and feel of the menu on the left.

The logic, after login the header menu will add another page:

Before Login:
Home / About / Trading / Support /

After Login
Home / About / Trading / Support / Account (Demo) - Logout

When you click on the / Account /

"Account Profile" page is loaded where you can change the settings etc.

"Account Profile" menu on the left should look the same as in / About / (https://mvb.co.uk/about/)

We need the following sub-pages under "Account Profile"

- Profile
- Transfers
- Reports
- Security
- API Key
- Affiliates

Now looking into each page:
-
- Profile (Should be split into individual or business) a user can choose whether how he want to run his account:

[Individual]

Personal Details
First Name:
Middle Name:
Family Name:
Citizenship:
Gender:
DOB:

[Attach File] (Government Issues ID, Passport, Driving License) - Verify

Contact Information
Phone: +44 207 555 0148 - Verify
E-Mail: sample@postvane.example - Verify

Residential Address
Address line 1:
Address line 2:
Address line 3:
City:
Postcode:
Country:

[Attach File] (Utility Bill or Bank Statement) - Verify

[Business]

Company Name:
Registration Number:

Registered Address
Address line 1:
Address line 2:
Address line 3:
City:
Postcode:
Country:

[Attach File] (Certificate of Incorporation) - Verify
[Attach File] (Memorandum & Articles of Association)
[Attach File] (Shareholder Register)

Company Contact Information
Website:

-

- Transfers (Where a user can link a bank account to deposit or withdraw funds from the account)

Transfers

Add a bank account:

Please select the country where beneficiary’s bank is domicile: [Please select]
Please select the currency you wish to make transfers in: [Please select]

Full beneficiary name:
Full beneficiary address:
Beneficiary bank name:
Beneficiary bank address:
Beneficiary Bank Identification Code (BIC)/Routing Code:
Beneficiary IBAN number/account number:

[SAVE]

Deposti funds to MVB Bank Account
Amount of currency to be received e.g. 2345.67 [Please select: USD, EUR, GBP] :
Full beneficiary name: Meridian Value Bourse Limited
Full beneficiary address: Quarrystone Court
7-9 Fenwick Lane
London, United Kingdom
Beneficiary bank name:
Beneficiary bank address:
Beneficiary Bank Identification Code (BIC)/Routing Code: XXXXXXXXXX
Beneficiary IBAN number/account number: XXXXXXXXXXXXXXXXXXXXXXXXXX

Deposit coins to MVB Coin Account
Amount of coins to be received e.g. 2345.67 [Please select: BTC, LTC]:
MVB Coin Account: XXXXXXXXXXXXXXXXXXXXXXXXXXXXX

Applicable charges (?):
[Clear] [Continue]

Withdraw funds from MVB Bank Account
Amount of currency to be sent e.g. 2345.67 [Please select: USD, EUR, GBP] :

Withdraw coins from MVB Coin Account:
Amount of coins to be sent e.g. 2345.67 [Please select: BTC, LTC]:
Please specify you coin account: XXXXXXXXXXXXXXXXXXXXXXXXXXXXX

Applicable charges (?):
[Clear] [Continue]

-

- Reports

TBC
-

- Security

Change Password
Current Password:
New Password:
Confirm New Password:

Enable / Disable : Two-factor Authentication (SMS)

-

- API Key
TBC

-
- Affiliates

Unlimited earning potential!
You'll receive up to 10% commission on all trades made through your affiliate link.

Orbit Referral Circle
Simply apply to our program from your publisher account or click the "Join Now" button below.

Lumenstack.com - Join Now

```html
<!DOCTYPE html>
<html lang="en">
<head>
<meta charset="utf-8">
<title>Meridian Value Bourse – Account Profile</title>
<link href="https://fonts.googleapis.com/css2?family=Arimo:wght@400;700&display=swap" rel="stylesheet">
<style>
:root{
  --backdrop:#333333;
  --paper:#ffffff;
  --brand:#009bd4;
  --ink:#2b2b2b;
  --muted:#7a7a7a;
  --nav:#555555;
  --field-line:#c4c4c4;
  --btn-dark:#474747;
  --rule:#7fcbe8;
}
*{box-sizing:border-box;margin:0;padding:0}
html,body{width:1200px;height:785px;overflow:hidden;background:var(--backdrop);font-family:"Arimo",Arial,sans-serif}
.page{position:absolute;left:66px;top:0;width:1068px;height:750px;background:var(--paper)}
.site-header{position:absolute;left:0;top:0;width:1068px;height:91px}
.brand-name{position:absolute;left:98px;top:26px;font-size:15px;line-height:18px;color:var(--ink);white-space:nowrap}
.brand-dot{position:absolute;left:272px;top:29px;width:12px;height:12px;border-radius:50%;background:var(--brand)}
.main-nav{position:absolute;left:254px;top:59px;font-size:11px;color:var(--nav);white-space:nowrap}
.field{position:absolute;top:36px;width:117px;height:23px;border:1px solid var(--field-line);border-radius:2px;font-size:11.5px;color:#9a9a9a;padding:4px 4px}
.field .hint{position:absolute;right:10px;top:4px;width:14px;height:14px;border:1px solid #bbb;border-radius:50%;font-size:9px;line-height:12px;text-align:center;color:#999}
.btn{position:absolute;top:36px;height:21px;border-radius:3px;color:#fff;font-size:9.5px;line-height:21px;text-align:center}
.btn-login{left:867px;width:50px;background:var(--btn-dark)}
.btn-signup{left:920px;width:49px;background:var(--brand)}
.ticker{position:absolute;left:0;top:91px;width:1068px;height:43px;background:var(--brand);color:#fff}
.coin{position:absolute;left:212px;top:6px;width:29px;height:29px;border-radius:50%;border:2px solid #fff}
.stat{position:absolute;top:7px;white-space:nowrap}
.stat-label{font-size:9.5px;font-weight:700;display:block;line-height:12px}
.stat-value{font-size:12.5px;display:block;line-height:17px}
.stat-value small{font-size:8.5px}
.ticker-rule{position:absolute;top:0;width:1px;height:43px;background:var(--rule)}
.content-title{position:absolute;left:191px;top:188px;font-size:18px;font-weight:700;color:var(--ink)}
.side-menu{position:absolute;left:170px;top:231px;width:100px;list-style:none;text-align:right}
.side-menu li{height:28.6px;font-size:14.5px;font-weight:700;color:var(--muted)}
.side-menu li.active{color:var(--ink)}
.active-bar{position:absolute;left:295px;top:286px;width:2px;height:23px;background:var(--ink)}
.panel-text{position:absolute;left:390px;top:233px;font-size:12.5px;font-weight:700;color:var(--ink)}
.site-footer{position:absolute;left:0;top:456px;width:1068px;height:294px;background:var(--brand);color:#fff}
.foot-name{position:absolute;left:98px;top:54px;font-size:15px;line-height:18px;white-space:nowrap}
.foot-dot{position:absolute;left:272px;top:57px;width:12px;height:12px;border-radius:50%;background:#fff}
.copyright{position:absolute;left:98px;top:109px;font-size:9.5px;line-height:13px}
.foot-col{position:absolute;top:40px}
.foot-col h3{font-size:19.5px;font-weight:700;margin-bottom:9px;line-height:20px}
.foot-col ul{list-style:none;font-size:11px;line-height:13.4px}
.social{position:absolute;top:71px;width:25px;height:25px;border-radius:50%;background:#fff}
.tagline-art{position:absolute;left:450px;top:185px;width:508px;height:68px;border-radius:6px;background:linear-gradient(90deg,rgba(255,255,255,.08),rgba(255,255,255,.22),rgba(255,255,255,.08))}
</style>
</head>
<body>
<div class="page">
  <header class="site-header">
    <div class="brand-name">Meridian Value Bourse</div>
    <div class="brand-dot"></div>
    <nav class="main-nav">Home · About · Trading &nbsp;· Support &nbsp;· Account (Demo) - Logout</nav>
    <div class="field" style="left:618px">Email<span class="hint">?</span></div>
    <div class="field" style="left:742px">Password<span class="hint">?</span></div>
    <div class="btn btn-login">Log In</div>
    <div class="btn btn-signup">Sign Up</div>
  </header>

  <section class="ticker">
    <div class="coin" role="img" aria-label="Coin symbol"></div>
    <div class="stat" style="left:251px"><span class="stat-label">Current Price</span><span class="stat-value">$444.13</span></div>
    <div class="ticker-rule" style="left:329px"></div>
    <div class="stat" style="left:352px"><span class="stat-label">Daily Change</span><span class="stat-value">-9.54 <small>2.10%</small></span></div>
    <div class="ticker-rule" style="left:440px"></div>
    <div class="stat" style="left:464px"><span class="stat-label">Day's Range</span><span class="stat-value">$440.00 - $457.30</span></div>
    <div class="ticker-rule" style="left:590px"></div>
    <div class="stat" style="left:613px"><span class="stat-label">Today's Open</span><span class="stat-value">$453.57</span></div>
    <div class="ticker-rule" style="left:696px"></div>
    <div class="stat" style="left:718px"><span class="stat-label">24h Volume</span><span class="stat-value">7194 BTC</span></div>
  </section>

  <h1 class="content-title">Account Profile</h1>
  <ul class="side-menu">
    <li>Profile</li>
    <li>Transfers</li>
    <li class="active">Reports</li>
    <li>Security</li>
    <li>API Key</li>
    <li>Affiliates</li>
  </ul>
  <div class="active-bar"></div>
  <p class="panel-text">TBC</p>

  <footer class="site-footer">
    <div class="foot-name">Meridian Value Bourse</div>
    <div class="foot-dot"></div>
    <p class="copyright">© 2014 Meridian Value Bourse.<br>All rights reserved</p>
    <div class="foot-col" style="left:400px">
      <h3>ABOUT US</h3>
      <ul><li>Rulebook</li><li>Trading Fees</li><li>Partners</li><li>Security</li><li>Terms of Service</li><li>Privacy Policy</li><li>Latest News</li></ul>
    </div>
    <div class="foot-col" style="left:628px">
      <h3>SUPPORT</h3>
      <ul><li>What is Bitcoin?</li><li>How to buy a bitcoin?</li><li>How to sell a bitcoin?</li></ul>
    </div>
    <div class="foot-col" style="left:833px"><h3>FOLLOW MVB</h3></div>
    <div class="social" style="left:833px" role="img" aria-label="Social link"></div>
    <div class="social" style="left:868px" role="img" aria-label="Social link"></div>
    <div class="social" style="left:905px" role="img" aria-label="Social link"></div>
    <div class="social" style="left:940px" role="img" aria-label="Social link"></div>
    <div class="tagline-art" role="img" aria-label="Hand-lettered tagline: Change the world one bitcoin at a time"></div>
  </footer>
</div>
</body>
</html>
```